mothers day ad for martial arts school

I am looking to have a nice flyer/handout to promote my martial arts school. It is for our promotion of "mom's train free" for mothers day in May. I would like an ad that would inspire a mother to learn self defense and to improve their fitness. It can have pictures but not necessarily a requirement. Pictures don't have to be of a lady in a martial arts uniform. It may be better if they are not. It also doesn't have to be standard sheet of paper size, as these are going to be handouts the size can be smaller. I would like our Crane Hollow logo on the flyer.

Target Market(s)

mothers that hadn't thought about martial arts before but would be convinced to try it

Industry/Entity Type

School

Requirements
Must have
• text, photos that would appeal to and encourage a mother to try a self defense/fitness class
Nice to have
• our logo and text and possibly pictures that would inspire a mother to join a martial arts class

```html
<!DOCTYPE html>
<html lang="en">
<head>
<meta charset="utf-8">
<title>Crane Hollow Martial Arts – Mother's Day Flyer</title>
<link href="https://fonts.googleapis.com/css2?family=Russo+One&family=Play:wght@400;700&display=swap" rel="stylesheet">
<style>
  :root {
    --red: #d7242f;
    --dark: #2b2b2d;
    --darker: #1f1f21;
    --white: #ffffff;
    --page: #3a3a3a;
  }
  html, body {
    margin: 0;
    width: 1200px;
    height: 1200px;
    overflow: hidden;
    background: var(--page);
  }
  .flyer {
    position: absolute;
    left: 200px;
    top: 35px;
    width: 800px;
    height: 1130px;
    overflow: hidden;
    background: var(--white);
    box-shadow: 0 20px 50px rgba(0,0,0,.45);
  }
  .flyer-art {
    position: absolute;
    inset: 0;
    width: 800px;
    height: 1130px;
  }
  .brand {
    position: absolute;
    left: 46px;
    top: 52px;
    display: flex;
    align-items: center;
    gap: 14px;
  }
  .brand-dot {
    width: 34px;
    height: 34px;
    border-radius: 50%;
    background: var(--red);
  }
  .brand-name {
    font-family: "Russo One", sans-serif;
    font-size: 40px;
    color: var(--white);
    letter-spacing: 1px;
  }
  .headline {
    position: absolute;
    left: 40px;
    top: 300px;
    margin: 0;
    font-family: "Russo One", sans-serif;
    font-weight: 400;
    line-height: .95;
    transform: rotate(7deg);
    transform-origin: left top;
  }
  .headline span { display: block; }
  .headline .accent { color: var(--red); }
  .headline .base { color: var(--dark); }
  .headline .l1 { font-size: 92px; }
  .headline .l2 { font-size: 56px; }
  .headline .l3 { font-size: 72px; }
  .headline .l4 { font-size: 42px; }
  .offer {
    position: absolute;
    left: 430px;
    top: 905px;
    font-family: "Play", sans-serif;
    font-weight: 700;
    line-height: 1;
    transform: rotate(7deg);
    transform-origin: left top;
  }
  .offer p { margin: 0 0 4px; white-space: nowrap; }
  .offer .offer-title { color: var(--red); font-size: 38px; }
  .offer .offer-sub { color: var(--dark); font-size: 34px; }
  .offer .offer-call { color: var(--red); font-size: 26px; font-weight: 400; }
  .website {
    position: absolute;
    right: 34px;
    bottom: 24px;
    font-family: "Play", sans-serif;
    font-size: 17px;
    letter-spacing: 5px;
    color: var(--white);
  }
</style>
</head>
<body>
<div class="flyer">
  <svg class="flyer-art" viewBox="0 0 800 1130" xmlns="http://www.w3.org/2000/svg">
    <defs>
      <linearGradient id="bg-light" x1="0" y1="0" x2="0" y2="1">
        <stop offset="0" stop-color="#e2e2e2"/>
        <stop offset=".6" stop-color="#f6f6f6"/>
        <stop offset="1" stop-color="#e9e9e9"/>
      </linearGradient>
      <linearGradient id="photo-dojo" x1="0" y1="0" x2="1" y2="1">
        <stop offset="0" stop-color="#f2f2f2"/>
        <stop offset=".55" stop-color="#c9c9cb"/>
        <stop offset="1" stop-color="#8e8e92"/>
      </linearGradient>
      <radialGradient id="photo-kid" cx=".5" cy=".45" r=".6">
        <stop offset="0" stop-color="#f0f0f0"/>
        <stop offset="1" stop-color="#a9a9ab"/>
      </radialGradient>
      <radialGradient id="photo-kick" cx=".5" cy=".5" r=".6">
        <stop offset="0" stop-color="#dedede"/>
        <stop offset="1" stop-color="#f4f4f4"/>
      </radialGradient>
    </defs>

    <rect class="field" x="0" y="0" width="800" height="720" fill="url(#bg-light)"/>

    <polygon class="top-band" points="0,0 800,0 800,95 0,220" fill="var(--dark)"/>
    <polygon class="top-stripe" points="0,220 800,95 800,110 0,238" fill="var(--red)"/>
    <polygon points="60,250 230,225 230,245 60,270" fill="var(--white)"/>

    <g role="img" aria-label="Photo of two adults in white uniforms practising a self-defence block in a bright dojo">
      <polygon points="240,196 800,120 800,660" fill="url(#photo-dojo)"/>
    </g>
    <polygon class="photo-edge" points="228,192 240,196 800,660 800,676" fill="var(--red)"/>

    <polygon class="mid-band" points="0,700 800,640 800,720 0,770" fill="var(--dark)"/>
    <polygon class="mid-stripe" points="0,770 800,720 800,732 0,782" fill="var(--red)"/>

    <g role="img" aria-label="Photo of a woman in a white uniform and black belt performing a side kick">
      <rect x="30" y="830" width="320" height="200" rx="8" fill="url(#photo-kick)"/>
    </g>

    <circle cx="470" cy="790" r="104" fill="var(--red)"/>
    <circle cx="470" cy="790" r="96" fill="var(--white)"/>
    <g role="img" aria-label="Photo of a girl in a white uniform with a red belt in a low stance">
      <circle cx="470" cy="790" r="89" fill="url(#photo-kid)"/>
    </g>
    <circle cx="688" cy="768" r="116" fill="var(--red)"/>
    <circle cx="688" cy="768" r="108" fill="var(--white)"/>
    <g role="img" aria-label="Photo of a boy in a white uniform tying his belt">
      <circle cx="688" cy="768" r="100" fill="url(#photo-kid)"/>
    </g>

    <polygon class="foot-red" points="0,970 400,1058 0,1058" fill="var(--red)"/>
    <polygon class="foot-band" points="0,1030 800,1078 800,1130 0,1130" fill="var(--darker)"/>
    <polygon class="foot-stripe" points="300,1060 800,1066 800,1073 300,1066" fill="var(--red)"/>
  </svg>

  <div class="brand">
    <span class="brand-dot"></span>
    <span class="brand-name">CRANE HOLLOW</span>
  </div>

  <h1 class="headline">
    <span class="accent l1">Learn</span>
    <span class="base l2">Self-Defence</span>
    <span class="accent l3">&amp; Fitness</span>
    <span class="base l4">Through Martial Arts</span>
  </h1>

  <div class="offer">
    <p class="offer-title">Moms train free</p>
    <p class="offer-sub">this mothers day</p>
    <p class="offer-call">Call us at 555.201.84</p>
  </div>

  <div class="website">cranehollowmartialarts.com</div>
</div>
</body>
</html>
```